Process Engineering/Construction Firm wants a OneSheet targeting craft brewers in Texas

We need a OneSheet (standard letter size) that we can share with craft brewers in our state, that explains what we can do for them. This will be shared primarily via email and online. We would like to see this be fun and modern flyer while still maintaining our professional vibe. More info and logos are uploaded - please review. Also, this project could lead to more branded documents from OneSheets to letterhead. We have our website and our logo(s) and really not much else that is consistent. There is certainly opportunity to work long-term.
Updates

Please note that the website listed on the flyer should read www.halvernworksadvisory.com. It will NOT follow the same domain name as the email address. And also, please DO NOT send me anything through the sales@hwaadvisoryllc.com email address at this time. I am trying to find a brewery-specific photo to use and will upload once found. I will be uploading shortly another logo of an affiliate organization we belong to - the Lone Kettle Brewing Alliance that I would like to see included on the flyer with the words, "A proud member of the Lone Kettle Brewing Alliance' OR just 'Proud Member.'

Target Market(s)

Craft brewery owners in Texas

Industry/Entity Type

Engineering

Font styles to use
Sans Serif

Requirements
Must have
• We need our point of contact to list the website as well as this email: sales@hwaadvisoryllc.com
• Maroon CMYK is: 32, 100, 82, 30
• We want these Brewery Specific service points included:
• • Brewhouse automation
• • Glycol systems
• • Complete line design and install
• • Packaging solutions
• • Epoxy & urethane flooring
• • New construction
• • Network of industry professionals
Nice to have
• Trendy and modern look to correlate with current craft beer logos and design trends

```html
<!DOCTYPE html>
<html lang="en">
<head>
<meta charset="utf-8">
<title>Halvern Works Advisory — Brewery Services</title>
<link rel="stylesheet" href="https://fonts.googleapis.com/css2?family=Gafata&family=Sorts+Mill+Goudy&display=swap">
<style>
  :root {
    --maroon: #7a0020;
    --maroon-deep: #1c0207;
    --ink: #000000;
    --paper: #ffffff;
    --amber: #f29a12;
    --amber-dark: #2a1604;
    --copper: #9a5a2e;
    --steel: #2c3436;
  }
  * { margin: 0; padding: 0; box-sizing: border-box; }
  html, body { width: 927px; height: 1200px; overflow: hidden; background: var(--paper); }
  .sheet { position: relative; width: 927px; height: 1200px; background: var(--paper); }
  .band { position: absolute; left: 60px; width: 468px; }
  .band--top { top: 32px; height: 16px; background: var(--maroon); }
  .band--under-title { top: 221px; height: 33px; background: var(--maroon); }
  .band--footer { top: 1060px; height: 31px; background: var(--maroon-deep); }
  .brand {
    position: absolute; left: 60px; top: 78px; width: 468px;
    text-align: center; color: var(--maroon);
    font-family: "Gafata", sans-serif; font-size: 50px; line-height: 56px;
    letter-spacing: -0.5px;
  }
  .services {
    position: absolute; left: 60px; top: 266px; width: 468px; height: 781px;
    background: linear-gradient(to bottom, var(--maroon) 0%, var(--maroon) 78%, var(--maroon-deep) 100%);
    list-style: none; padding-top: 58px;
  }
  .services li {
    color: var(--paper); text-align: center;
    font-family: "Sorts Mill Goudy", serif; font-size: 23px;
    height: 84.3px; line-height: 30px;
  }
  .web-bar {
    position: absolute; left: 60px; top: 1102px; width: 468px; height: 57px;
    background: var(--ink); color: var(--paper);
    font-family: "Sorts Mill Goudy", serif; font-size: 19px;
    display: flex; align-items: center; justify-content: center;
  }
  .contact {
    position: absolute; left: 560px; top: 1122px; width: 340px;
    font-family: "Sorts Mill Goudy", serif; font-size: 19px; color: var(--ink);
    text-align: center; white-space: nowrap;
  }
  .photo { position: absolute; left: 597px; width: 271px; }
  .photo--beer { top: 32px; height: 361px;
    background: linear-gradient(100deg, var(--amber-dark) 0%, #c96a05 22%, var(--amber) 45%, #f5b21a 70%, #ef8a10 100%); }
  .photo--brewhouse { top: 469px; height: 181px;
    background: linear-gradient(to bottom, #d9d6d0 0%, #3a2a20 25%, var(--copper) 55%, #2a2624 85%, #1a1c20 100%); }
  .photo--cellar { top: 727px; height: 320px;
    background: linear-gradient(to bottom, #8c9490 0%, var(--steel) 45%, #3b3020 75%, #22261f 100%); }
</style>
</head>
<body>
<main class="sheet">
  <div class="band band--top"></div>
  <h1 class="brand">Halvern Works<br>Advisory</h1>
  <div class="band band--under-title"></div>

  <ul class="services">
    <li>Brewhouse automation</li>
    <li>Glycol systems</li>
    <li>Complete line design and install</li>
    <li>Packaging solutions</li>
    <li>Epoxy &amp; urethane flooring</li>
    <li>New construction</li>
    <li>Network of&nbsp; industry professionals</li>
  </ul>

  <div class="band band--footer"></div>
  <div class="web-bar">http://www.halvernworksadvisory.com</div>

  <div class="photo photo--beer" role="img" aria-label="Close-up photo of golden beer with rising bubbles in a glass"></div>
  <div class="photo photo--brewhouse" role="img" aria-label="Photo of copper brewhouse kettles on a raised platform"></div>
  <div class="photo photo--cellar" role="img" aria-label="Photo of a large steel tank above rows of wooden barrels on a stone floor"></div>

  <p class="contact">Contact: sales@hwaadvisoryllc.com</p>
</main>
</body>
</html>
```